Restaurant service company needs a website!

I am looking for a skilled web designer/developer to create a professional, responsive, and easy-to-navigate website for my company, which specializes in servicing restaurant cooking equipment. The site should communicate trust, reliability, and technical expertise to our target audience, restaurant owners, managers, and commercial kitchen operators. I have included the company logos, if any other format for them is needed please let me know.

Target Market(s)

restaurant owners, managers, and commercial kitchen operators

Industry/Entity Type

Commercial Kitchen Equipment Service

Coding

Coded - Design and coding required

Number of Pages Required

1 page

Font styles to use
Serif
Sans Serif

Requirements
Must have
• Contact and service request forms, Click-to-call functionality for mobile, Clean, modern layout with strong visuals, Easy navigation, mobile-friendly
Nice to have
• Testimonials or Reviews, If possible a click-to-text functionality for mobile.
Should not have
• Any mention of Refrigeration or HVAC, "Free Quotes"

```html
<!DOCTYPE html>
<html lang="en">
<head>
<meta charset="UTF-8">
<title>HEARTHLINE – Premium Equipment Service</title>
<link href="https://fonts.googleapis.com/css2?family=Inter:ital,wght@0,400;0,500;0,600;0,700;1,400&display=swap" rel="stylesheet">
<style>
:root{
  --teal:#0b5d73;
  --teal-dark:#084a5c;
  --orange:#ff6a33;
  --ink:#1f2328;
  --muted:#6b7380;
  --soft:#f5f7f9;
  --line:#e2e6ea;
  --footer:#1e1e1e;
  --white:#ffffff;
}
*{box-sizing:border-box;margin:0;padding:0}
html,body{width:1200px;height:4552px;overflow:hidden}
body{font-family:"Inter",sans-serif;color:var(--ink);background:var(--white);font-size:14px}
.wrap{width:930px;margin:0 auto}
a{color:inherit;text-decoration:none}

/* nav */
.nav{height:67px;display:flex;align-items:center;justify-content:space-between;padding:0 105px 0 124px;background:var(--white);box-shadow:0 1px 4px rgba(0,0,0,.06);position:relative;z-index:2}
.brand{display:flex;align-items:center;gap:8px;font-weight:700;font-size:20px;color:var(--teal)}
.brand-mark{width:32px;height:32px;border-radius:6px;background:var(--teal)}
.nav-links{display:flex;align-items:center;gap:26px;font-size:13px;font-weight:500}
.btn{display:inline-flex;align-items:center;justify-content:center;gap:8px;border-radius:6px;font-weight:600;font-size:13px}
.btn-orange{background:var(--orange);color:var(--white)}
.nav .btn{height:36px;padding:0 16px}

/* hero */
.hero{height:580px;position:relative;color:var(--white);text-align:center;background:linear-gradient(120deg,#0f5f74,#1c7688 45%,#0a5468)}
.hero-photo{position:absolute;inset:0;background:radial-gradient(circle at 70% 30%,rgba(255,255,255,.12),transparent 45%),radial-gradient(circle at 20% 20%,rgba(255,255,255,.08),transparent 35%)}
.hero-inner{position:relative;padding-top:136px}
.hero h1{font-size:44px;line-height:1.12;font-weight:700}
.hero p{width:470px;margin:28px auto 0;font-size:14.5px;line-height:1.7;opacity:.92}
.hero-actions{display:flex;justify-content:center;gap:16px;margin-top:30px}
.hero-actions .btn{height:44px;padding:0 24px}
.btn-ghost{border:1.5px solid var(--white);color:var(--white)}
.stats{display:flex;justify-content:center;gap:54px;margin-top:54px}
.stat strong{display:block;font-size:32px;font-weight:700}
.stat span{display:block;font-size:11px;letter-spacing:1px;margin-top:8px;opacity:.85}

/* section heads */
.section-head{text-align:center}
.section-head h2{font-size:31px;font-weight:700}
.section-head h2::after{content:"";display:block;width:60px;height:3px;margin:14px auto 0;background:linear-gradient(90deg,var(--teal),var(--orange))}
.section-head p{width:560px;margin:24px auto 0;font-size:12.5px;line-height:1.65;color:var(--muted)}

/* services */
.services{height:793px;background:var(--soft);padding-top:78px}
.service-grid{display:flex;gap:24px;margin-top:56px;padding:0 4px}
.service-card{width:293px;height:517px;background:var(--white);border-radius:6px;box-shadow:0 4px 16px rgba(0,0,0,.08);overflow:hidden;display:flex;flex-direction:column}
.service-top{height:158px;background:var(--teal);display:flex;align-items:center;justify-content:center}
.service-body{padding:22px 24px;flex:1;display:flex;flex-direction:column}
.service-body h3{font-size:21px;color:var(--teal);font-weight:700}
.service-body p{font-size:12px;color:var(--muted);line-height:1.65;margin-top:14px}
.checks{list-style:none;margin-top:16px}
.checks li{font-size:12px;line-height:26.5px;display:flex;gap:8px;align-items:center}
.checks li::before{content:"✓";color:var(--orange);font-weight:700}
.service-body .btn{margin-top:auto;height:42px;background:var(--teal);color:var(--white);font-size:12px}

/* why */
.why{height:548px;padding-top:76px}
.why-grid{display:flex;gap:32px;margin-top:58px;justify-content:center}
.why-card{width:287px;height:258px;border-top:3px solid;border-image:linear-gradient(90deg,var(--teal),var(--orange)) 1;box-shadow:0 4px 16px rgba(0,0,0,.08);text-align:center;padding:28px 24px}
.why-card h3{font-size:22px;font-weight:700;margin-top:14px}
.why-card p{font-size:12px;color:var(--muted);line-height:1.7;margin-top:16px}

/* process */
.process{height:504px;background:var(--soft);padding-top:64px}
.steps{display:flex;justify-content:center;margin-top:58px;position:relative;width:714px;margin-left:auto;margin-right:auto}
.steps::before{content:"";position:absolute;left:0;right:0;top:31px;height:1px;background:var(--line)}
.step{width:178px;text-align:center;position:relative;padding:0 12px}
.step-num{width:63px;height:63px;border-radius:50%;background:var(--teal);color:var(--white);font-weight:700;font-size:22px;display:flex;align-items:center;justify-content:center;margin:0 auto}
.step h3{font-size:21px;color:var(--teal);line-height:1.25;margin-top:16px;font-weight:700}
.step p{font-size:12px;color:var(--muted);line-height:1.65;margin-top:10px}

/* testimonials */
.testimonials{height:521px;padding-top:52px}
.testi-grid{display:flex;gap:26px;margin-top:56px;justify-content:center}
.testi-card{width:292px;height:292px;box-shadow:0 4px 16px rgba(0,0,0,.09);border-radius:6px;padding:30px 24px}
.testi-card blockquote{font-style:italic;font-size:12px;color:var(--muted);line-height:1.7}
.person{display:flex;align-items:center;gap:14px;margin-top:24px}
.avatar{width:46px;height:46px;border-radius:50%;background:var(--teal);color:var(--white);font-weight:700;font-size:14px;display:flex;align-items:center;justify-content:center}
.person strong{display:block;font-size:12.5px}
.person span{font-size:11px;color:var(--muted)}

/* contact */
.contact{height:1110px;padding-top:90px}
.contact-grid{display:flex;justify-content:space-between;margin-top:52px;padding-left:12px}
.info{width:420px;padding-top:14px}
.info h3{font-size:23px;color:var(--teal);font-weight:700}
.info > p{font-size:12.5px;color:var(--muted);line-height:1.7;margin-top:16px}
.info-item{display:flex;gap:14px;margin-top:26px}
.info-item svg{flex:none;margin-top:2px}
.info-item strong{font-size:12.5px;display:block}
.info-item .val{font-size:13px;color:var(--teal);margin-top:16px;display:block}
.info-item .sub{font-size:12.5px;color:var(--muted);margin-top:16px;line-height:1.6}
.info-item small{display:block;font-size:11px;color:var(--muted);margin-top:22px}
.form-card{width:444px;height:849px;box-shadow:0 4px 20px rgba(0,0,0,.08);border-radius:8px;padding:28px 34px;margin-top:-13px}
.form-card h3{font-size:23px;font-weight:700}
.field{margin-top:18px}
.field:first-of-type{margin-top:12px}
.field label{display:block;font-size:12px;font-weight:600;margin-bottom:12px}
.field input,.field select,.field textarea{width:100%;height:40px;border:1px solid var(--line);border-radius:6px;font-family:inherit;font-size:12.5px;padding:0 14px;background:var(--white)}
.field textarea{height:118px;resize:vertical}
.submit{width:100%;height:36px;margin-top:24px;border:0;background:var(--orange);color:var(--white);font-family:inherit;font-weight:600;font-size:12.5px;border-radius:6px}

/* footer */
.footer{height:429px;background:var(--footer);color:#d7d7d7;padding-top:60px}
.foot-grid{display:flex;justify-content:space-between}
.foot-col{width:290px}
.foot-col h4{font-size:22px;color:var(--white);font-weight:700}
.foot-col h4::after{content:"";display:block;width:36px;height:3px;background:var(--orange);margin-top:12px}
.foot-col p{font-size:12.5px;line-height:1.75;margin-top:20px}
.foot-col ul{list-style:none;margin-top:16px}
.foot-col li{font-size:12.5px;line-height:30px}
.foot-contact li{display:flex;align-items:center;gap:12px;line-height:60px}
.socials{display:flex;gap:14px;margin-top:22px}
.socials span{width:30px;height:30px;border-radius:50%;background:#3a3a3a}
.copyright{border-top:1px solid #333;margin-top:104px;padding-top:20px;text-align:center;font-size:11px;color:#999}
</style>
</head>
<body>

<header class="nav">
  <a class="brand" href="#"><span class="brand-mark"></span>HEARTHLINE</a>
  <nav class="nav-links">
    <a href="#">Home</a><a href="#services">Services</a><a href="#process">Process</a><a href="#testimonials">Testimonials</a>
    <a class="btn btn-orange" href="#contact">Contact Us</a>
  </nav>
</header>

<section class="hero">
  <div class="hero-photo" role="img" aria-label="Chef working in a commercial kitchen, tinted teal"></div>
  <div class="hero-inner">
    <h1>Premium Equipment Service<br>for Elite Restaurants</h1>
    <p>Trusted by award-winning establishments and leading hotel chains for expert equipment maintenance and rapid emergency repairs.</p>
    <div class="hero-actions">
      <a class="btn btn-orange" href="#contact">
        <svg width="13" height="13" viewBox="0 0 14 14"><rect x="1" y="2" width="12" height="11" rx="1.5" fill="#fff"/><rect x="1" y="5" width="12" height="1.5" fill="#ff6a33"/></svg>Schedule Service</a>
      <a class="btn btn-ghost" href="tel:5550142290">
        <svg width="13" height="13" viewBox="0 0 24 24"><path d="M6.6 10.8a15 15 0 0 0 6.6 6.6l2.2-2.2c.3-.3.7-.4 1-.2 1.1.4 2.3.6 3.6.6.6 0 1 .4 1 1V20c0 .6-.4 1-1 1C10.6 21 3 13.4 3 4c0-.6.4-1 1-1h3.5c.6 0 1 .4 1 1 0 1.3.2 2.5.6 3.6.1.3 0 .7-.2 1z" fill="#fff"/></svg>Emergency Line</a>
    </div>
    <div class="stats">
      <div class="stat"><strong>24/7</strong><span>EMERGENCY SERVICE</span></div>
      <div class="stat"><strong>98%</strong><span>FIRST-TIME FIX RATE</span></div>
      <div class="stat"><strong>45min</strong><span>AVG. RESPONSE TIME</span></div>
    </div>
  </div>
</section>

<section class="services" id="services">
  <div class="wrap">
    <div class="section-head">
      <h2>Our Premium Services</h2>
      <p>Comprehensive solutions for the most demanding commercial kitchens. We service all major equipment brands with factory-trained technicians.</p>
    </div>
    <div class="service-grid">
      <article class="service-card">
        <div class="service-top"><svg width="40" height="44" viewBox="0 0 40 44"><path d="M20 2c3 9 16 14 16 26a16 16 0 0 1-32 0c0-7 4-11 7-14 0 5 2 8 5 8 0-8 0-14 4-20z" fill="#fff"/><circle cx="20" cy="31" r="6" fill="#0b5d73"/></svg></div>
        <div class="service-body">
          <h3>Cooking Equipment</h3>
          <p>Expert maintenance and repair for high-end commercial ranges, ovens, and specialty cooking equipment.</p>
          <ul class="checks"><li>Gas and electric range repair</li><li>Convection &amp; combi oven calibration</li><li>Pilot light and ignition issues</li><li>Temperature control problems</li><li>Broiler and salamander service</li></ul>
          <a class="btn" href="#contact">Request Service</a>
        </div>
      </article>
      <article class="service-card">
        <div class="service-top"><svg width="44" height="44" viewBox="0 0 44 44"><rect x="6" y="4" width="26" height="12" rx="2" fill="#fff"/><rect x="14" y="16" width="10" height="8" fill="#fff"/><rect x="10" y="24" width="20" height="10" rx="2" fill="#fff"/><rect x="6" y="36" width="28" height="4" rx="1" fill="#fff"/><rect x="32" y="8" width="6" height="4" fill="#fff"/></svg></div>
        <div class="service-body">
          <h3>Food Prep Equipment</h3>
          <p>Comprehensive service for commercial mixers, slicers, food processors, and preparation equipment.</p>
          <ul class="checks"><li>Commercial mixer repair</li><li>Slicer blade sharpening</li><li>Food processor maintenance</li><li>Dough sheeter calibration</li><li>Vegetable prep equipment</li></ul>
          <a class="btn" href="#contact">Request Service</a>
        </div>
      </article>
      <article class="service-card">
        <div class="service-top"><svg width="44" height="44" viewBox="0 0 44 44"><rect x="14" y="4" width="10" height="26" rx="5" fill="none" stroke="#fff" stroke-width="3"/><circle cx="19" cy="34" r="7" fill="#fff"/><rect x="17.5" y="14" width="3" height="18" fill="#fff"/><circle cx="34" cy="8" r="3.5" fill="none" stroke="#fff" stroke-width="2.5"/></svg></div>
        <div class="service-body">
          <h3>Specialty Equipment</h3>
          <p>Expert maintenance for fryers, griddles, steamers, and other specialized cooking systems.</p>
          <ul class="checks"><li>Fryer oil filtration systems</li><li>Griddle surface maintenance</li><li>Steamer and kettle repair</li><li>Thermostat calibration</li><li>Ventilation system service</li></ul>
          <a class="btn" href="#contact">Request Service</a>
        </div>
      </article>
    </div>
  </div>
</section>

<section class="why">
  <div class="wrap">
    <div class="section-head">
      <h2>Why Elite Restaurants Choose Us</h2>
      <p>Experience the difference of premium service designed for establishments that cannot afford downtime.</p>
    </div>
    <div class="why-grid">
      <article class="why-card">
        <svg width="36" height="40" viewBox="0 0 36 40"><circle cx="18" cy="14" r="12" fill="#0b5d73"/><circle cx="18" cy="14" r="5" fill="#fff"/><path d="M10 24l-3 14 6-3 5 4 3-13zM26 24l3 14-6-3-5 4" fill="#0b5d73"/></svg>
        <h3>Certified Excellence</h3>
        <p>Our technicians hold certifications from leading equipment manufacturers including Ardent, Forgeline, and Kettlemark.</p>
      </article>
      <article class="why-card">
        <svg width="38" height="38" viewBox="0 0 38 38"><circle cx="19" cy="19" r="18" fill="#0b5d73"/><path d="M19 9v11l7 4" stroke="#fff" stroke-width="3" fill="none" stroke-linecap="round"/></svg>
        <h3>Priority Response</h3>
        <p>Guaranteed rapid response times with 24/7 emergency service. Average emergency response time is under 45 minutes.</p>
      </article>
      <article class="why-card">
        <svg width="40" height="40" viewBox="0 0 40 40"><path d="M6 34L26 14" stroke="#0b5d73" stroke-width="6" stroke-linecap="round"/><circle cx="30" cy="10" r="8" fill="#0b5d73"/><circle cx="33" cy="7" r="3.5" fill="#fff"/><path d="M8 6l26 26" stroke="#0b5d73" stroke-width="5" stroke-linecap="round"/><rect x="3" y="3" width="9" height="9" rx="2" fill="#0b5d73"/></svg>
        <h3>Genuine Parts</h3>
        <p>We use only manufacturer-approved parts to ensure optimal performance and longevity with 1-year warranty.</p>
      </article>
    </div>
  </div>
</section>

<section class="process" id="process">
  <div class="wrap">
    <div class="section-head">
      <h2>Our Service Process</h2>
      <p>Streamlined service designed to minimize your downtime and get your kitchen back to full operation quickly.</p>
    </div>
    <div class="steps">
      <div class="step"><div class="step-num">1</div><h3>Contact &amp; Diagnosis</h3><p>Call our emergency line or submit a service request. Our team will perform remote diagnosis when possible.</p></div>
      <div class="step"><div class="step-num">2</div><h3>Dispatch Technician</h3><p>We dispatch a certified technician with the right parts and tools for your specific equipment issue.</p></div>
      <div class="step"><div class="step-num">3</div><h3>Repair &amp; Testing</h3><p>Our technician performs the repair using genuine parts and thoroughly tests the equipment.</p></div>
      <div class="step"><div class="step-num">4</div><h3>Follow-up &amp; Support</h3><p>We follow up to ensure everything is working perfectly and provide ongoing maintenance recommendations.</p></div>
    </div>
  </div>
</section>

<section class="testimonials" id="testimonials">
  <div class="wrap">
    <div class="section-head">
      <h2>Client Testimonials</h2>
      <p>Hear from restaurant owners and chefs who trust us with their equipment.</p>
    </div>
    <div class="testi-grid">
      <article class="testi-card">
        <blockquote>"HEARTHLINE provides exceptional service that matches the quality of our establishment. Their technicians are knowledgeable, professional, and always arrive promptly. When our main oven failed during dinner service, they had us back up and running in under an hour."</blockquote>
        <div class="person"><div class="avatar">DO</div><div><strong>Daniel Okafor</strong><span>Owner, Maple Table</span></div></div>
      </article>
      <article class="testi-card">
        <blockquote>"The preventive maintenance program from HEARTHLINE has significantly reduced our equipment downtime. Their attention to detail is remarkable. We've seen a 40% reduction in emergency repairs since signing up for their premium maintenance plan."</blockquote>
        <div class="person"><div class="avatar">LM</div><div><strong>Lena Marsh</strong><span>Manager, Copper Pan</span></div></div>
      </article>
      <article class="testi-card">
        <blockquote>"As an executive chef, I can't afford equipment failures during service. HEARTHLINE understands this pressure and delivers reliable, expert service every time. Their technicians know commercial kitchen equipment inside and out."</blockquote>
        <div class="person"><div class="avatar">OR</div><div><strong>Owen Reyes</strong><span>Executive Chef, The Saltwater Room</span></div></div>
      </article>
    </div>
  </div>
</section>

<section class="contact" id="contact">
  <div class="wrap">
    <div class="section-head">
      <h2>Request Premium Service</h2>
      <p>Contact us for immediate assistance or to schedule maintenance. Our team is ready to help.</p>
    </div>
    <div class="contact-grid">
      <div class="info">
        <h3>Get In Touch</h3>
        <p>Our team is ready to provide the premium service your establishment deserves.</p>
        <div class="info-item">
          <svg width="14" height="14" viewBox="0 0 24 24"><path d="M6.6 10.8a15 15 0 0 0 6.6 6.6l2.2-2.2c.3-.3.7-.4 1-.2 1.1.4 2.3.6 3.6.6.6 0 1 .4 1 1V20c0 .6-.4 1-1 1C10.6 21 3 13.4 3 4c0-.6.4-1 1-1h3.5c.6 0 1 .4 1 1 0 1.3.2 2.5.6 3.6.1.3 0 .7-.2 1z" fill="#0b5d73"/></svg>
          <div><strong>Emergency Line</strong><a class="val" href="tel:5550142290">(555) 014-2290</a><small>Available 24/7 for emergency service</small></div>
        </div>
        <div class="info-item">
          <svg width="14" height="14" viewBox="0 0 24 24"><rect x="2" y="5" width="20" height="14" rx="2" fill="#0b5d73"/><path d="M3 6l9 7 9-7" stroke="#fff" stroke-width="1.6" fill="none"/></svg>
          <div><strong>Email Us</strong><a class="val" href="mailto:service@hearthlineservice.com">service@hearthlineservice.com</a><small>Typically respond within 1 hour during business hours</small></div>
        </div>
        <div class="info-item">
          <svg width="14" height="14" viewBox="0 0 24 24"><path d="M12 2a7 7 0 0 0-7 7c0 5 7 13 7 13s7-8 7-13a7 7 0 0 0-7-7z" fill="#0b5d73"/><circle cx="12" cy="9" r="2.6" fill="#fff"/></svg>
          <div><strong>Service Area</strong><div class="sub">Serving premium establishments throughout the region</div><small>Metro area and surrounding counties</small></div>
        </div>
        <div class="info-item">
          <svg width="14" height="14" viewBox="0 0 24 24"><circle cx="12" cy="12" r="10" fill="#0b5d73"/><path d="M12 6v7l4 2" stroke="#fff" stroke-width="2" fill="none"/></svg>
          <div><strong>Response Time</strong><div class="sub">Emergency calls: 45 minutes or less<br>Standard service: 24 hours</div><small>Guaranteed response times for premium clients</small></div>
        </div>
      </div>
      <form class="form-card">
        <h3>Service Request Form</h3>
        <div class="field"><label>Your Name</label><input type="text"></div>
        <div class="field"><label>Email Address</label><input type="email"></div>
        <div class="field"><label>Phone Number</label><input type="tel"></div>
        <div class="field"><label>Restaurant Name</label><input type="text"></div>
        <div class="field"><label>Equipment Type</label><select><option>Select Equipment Type</option></select></div>
        <div class="field"><label>Service Urgency</label><select><option>Select Urgency</option></select></div>
        <div class="field" style="margin-top:40px"><label>Describe the Issue</label><textarea></textarea></div>
        <button class="submit" type="submit">Submit Priority Request</button>
      </form>
    </div>
  </div>
</section>

<footer class="footer">
  <div class="wrap">
    <div class="foot-grid">
      <div class="foot-col">
        <h4>HEARTHLINE</h4>
        <p>Premium restaurant equipment service for establishments that demand excellence. Trusted by top-tier restaurants and commercial kitchens.</p>
        <div class="socials"><span></span><span></span><span></span></div>
      </div>
      <div class="foot-col">
        <h4>Services</h4>
        <ul><li>Range &amp; Oven Service</li><li>Food Prep Equipment</li><li>Specialty Cooking Equipment</li><li>Preventive Maintenance</li><li>Emergency Repairs</li></ul>
      </div>
      <div class="foot-col">
        <h4>Contact</h4>
        <ul class="foot-contact">
          <li><svg width="13" height="13" viewBox="0 0 24 24"><path d="M6.6 10.8a15 15 0 0 0 6.6 6.6l2.2-2.2c.3-.3.7-.4 1-.2 1.1.4 2.3.6 3.6.6.6 0 1 .4 1 1V20c0 .6-.4 1-1 1C10.6 21 3 13.4 3 4c0-.6.4-1 1-1h3.5c.6 0 1 .4 1 1 0 1.3.2 2.5.6 3.6.1.3 0 .7-.2 1z" fill="#1b7f99"/></svg>(555) 014-2290</li>
          <li><svg width="13" height="13" viewBox="0 0 24 24"><rect x="2" y="5" width="20" height="14" rx="2" fill="#1b7f99"/></svg>service@hearthlineservice.com</li>
          <li><svg width="13" height="13" viewBox="0 0 24 24"><circle cx="12" cy="12" r="10" fill="#1b7f99"/></svg>24/7 Emergency Service Available</li>
        </ul>
      </div>
    </div>
    <div class="copyright">© 2023 HEARTHLINE Premium Equipment Service. All Rights Reserved.</div>
  </div>
</footer>

</body>
</html>
```